Label for high-end indie coffee package

I need a label for high-end indie coffee package.

Coffee comes from Mt. Elgon, Trans-Nzoia County, Kenya. The coffee will be sold in Finland. The package as such will be semi matte black and the label will be printed out as a sticker.

Maximum measurements for the label would around 9 x 9 centimeters. It can be a square / rectangle / circle. I would like it to include influences from coffee origins (Kenya) and also demonstrate the high-end quality of the coffee with the modern twist.

The label should include the following text:

Coffee Name:
Morelu Vintaro AA
Washed & Natural

Origins:
Mt. Elgon, Trans-Nzoia County, Kenya

Growing altitude:
Altitude: 1 800 amsl

Coffee variety:
100 % Arabica

Following fields should be possible to be filled afterwards when the need occurs:
roast date
best before
roasted by

I'll be more than happy to answer any questions!

Finland. High-end customers, design coffee shops.

```html
<!DOCTYPE html>
<html lang="en">
<head>
<meta charset="utf-8">
<title>Morelu Vintaro AA – Coffee Label</title>
<link href="https://fonts.googleapis.com/css2?family=Playfair+Display:wght@700;800&family=Poppins:wght@400;600&family=Zilla+Slab:wght@700&display=swap" rel="stylesheet">
<style>
  :root {
    --backdrop: #636363;
    --gold-light: #f6c898;
    --gold-mid: #d9a06c;
    --gold-dark: #b98353;
    --face: #efefef;
    --ink: #242222;
    --line: #3a2e2a;
    --brown: #9a5c33;
    --cup: #2e1c18;
    --field-bg: #ffffff;
    --field-border: #cfcfcf;
  }
  * { box-sizing: border-box; margin: 0; padding: 0; }
  html, body { width: 720px; height: 1200px; overflow: hidden; }
  body { background: var(--backdrop); position: relative; }

  .label {
    position: absolute;
    left: 50px; top: 290px;
    width: 620px; height: 620px;
    border-radius: 50%;
    background: linear-gradient(160deg, var(--gold-light) 0%, var(--gold-mid) 30%, var(--gold-dark) 55%, var(--gold-mid) 80%, var(--gold-light) 100%);
  }
  .label-face {
    position: absolute;
    inset: 13px;
    border-radius: 50%;
    background: var(--face);
    overflow: hidden;
  }
  .landscape {
    position: absolute;
    left: 0; right: 0; top: 310px; bottom: 0;
    background: linear-gradient(180deg, rgba(239,239,239,0) 0%, #d8d8d8 25%, #bdbdbd 50%, #8a8a8a 75%, #4a4a4a 100%);
  }
  .inner-ring { position: absolute; inset: 0; }

  .title {
    position: absolute;
    left: 0; right: 0; top: 42px;
    text-align: center;
    font-family: "Playfair Display", serif;
    font-weight: 700;
    font-size: 58px;
    line-height: 56px;
    color: var(--ink);
    letter-spacing: 0.5px;
  }
  .cup {
    position: absolute;
    left: 227px; top: 175px;
    width: 140px; height: 56px;
    background: var(--cup);
    border-radius: 10px 10px 38px 38px;
  }
  .banner {
    position: absolute;
    left: 75px; top: 230px;
    width: 444px; height: 78px;
    background: var(--face);
    border: 3px solid var(--line);
    padding: 4px;
  }
  .banner-inner {
    width: 100%; height: 100%;
    border: 1.5px solid var(--line);
    display: flex; align-items: center; justify-content: center;
  }
  .process {
    font-family: "Zilla Slab", serif;
    font-weight: 700;
    font-size: 52px;
    color: var(--brown);
    transform: scaleX(0.8);
    white-space: nowrap;
    letter-spacing: 0.5px;
  }
  .origin {
    position: absolute;
    left: 0; right: 0; top: 318px;
    text-align: center;
    font-family: "Poppins", sans-serif;
    font-size: 20px;
    color: var(--ink);
  }
  .specs {
    position: absolute;
    left: 0; right: 0; top: 350px;
    text-align: center;
    font-family: "Poppins", sans-serif;
    font-weight: 600;
    font-size: 15px;
    color: var(--ink);
    word-spacing: 1px;
  }
  .specs .divider { margin: 0 12px; font-weight: 400; }
  .fields {
    position: absolute;
    left: 74px; top: 395px;
    display: flex; gap: 14px;
  }
  .field { width: 138px; text-align: center; }
  .field-label {
    font-family: "Playfair Display", serif;
    font-weight: 700;
    font-size: 15px;
    color: var(--ink);
    letter-spacing: 0.2px;
    margin-bottom: 6px;
    white-space: nowrap;
  }
  .field-box {
    height: 28px;
    background: var(--field-bg);
    border: 1px solid var(--field-border);
  }
</style>
</head>
<body>
  <div class="label">
    <div class="label-face">
      <div class="landscape" role="img" aria-label="Black and white Kenyan savanna landscape with an acacia tree and Mt. Elgon in the distance"></div>
      <svg class="inner-ring" viewBox="0 0 594 594" aria-hidden="true">
        <circle cx="297" cy="297" r="284" fill="none" stroke="var(--line)" stroke-width="1.5"/>
      </svg>

      <h1 class="title">MORELU<br>VINTARO AA</h1>
      <div class="cup" role="img" aria-label="Steaming coffee cup emblem"></div>

      <div class="banner">
        <div class="banner-inner">
          <span class="process">WASHED &amp; NATURAL</span>
        </div>
      </div>

      <p class="origin">Mt. Elgon, Trans-Nzoia County, Kenya</p>
      <p class="specs">Altitude: 1 800 amsl<span class="divider">|</span>100 % Arabica</p>

      <div class="fields">
        <div class="field">
          <div class="field-label">ROAST DATE</div>
          <div class="field-box"></div>
        </div>
        <div class="field">
          <div class="field-label">BEST BEFORE</div>
          <div class="field-box"></div>
        </div>
        <div class="field">
          <div class="field-label">ROASTED BY</div>
          <div class="field-box"></div>
        </div>
      </div>
    </div>
  </div>
</body>
</html>
```